Nanotechnology meets nature cosmetic company needs label design. Name of the company is QuillaBloom

We are a cosmetic brand that combines nanotechnology with nature in the form of hemp extracts and essential oils, creating products that provide pain relief as well as stress reduction and relaxation. We have three different products and need three separate labels. We have a logo and would like to incorporate that into the label design. The colors are teal, black and gray. We would like to convey a message of combining nature with cutting edge cosmetic technology.
1. Topical pain lotion
2. Bath soak
3. Massage lotion
The logo is attached and I would just like the logo used and not the text below. The colors of the logo should be teal cross and "V" inside the gray lines that make up the circle with black color inside the circle. If this can't be done, I can send another logo.

```html
<!DOCTYPE html>
<html lang="en">
<head>
<meta charset="utf-8">
<title>QuillaBloom – Label Designs</title>
<link rel="stylesheet" href="https://fonts.googleapis.com/css2?family=Josefin+Sans:wght@300;400;600&family=Montserrat:wght@300;400;600&display=swap">
<style>
  :root {
    --bg: #f6f6f6;
    --caption: #b4b4b4;
    --black: #161616;
    --black-soft: #2a2a2a;
    --divider: #6b6b6b;
    --teal: #3ab5a5;
    --teal-light: #5fc4b6;
    --white: #ffffff;
    --ink: #151515;
  }
  * { box-sizing: border-box; margin: 0; padding: 0; }
  html, body { width: 686px; height: 1200px; overflow: hidden; background: var(--bg); }
  body { position: relative; font-family: "Montserrat", sans-serif; color: var(--white); }

  .caption {
    position: absolute; left: 0; width: 686px; text-align: center;
    font-family: "Montserrat", sans-serif; font-weight: 400; font-size: 17px; color: var(--caption);
  }

  .label { position: absolute; overflow: hidden; background: var(--teal); }
  .label__top {
    position: absolute; left: 0; top: 0; width: 100%;
    background: radial-gradient(ellipse at 50% 40%, var(--black-soft) 0%, var(--black) 70%);
    display: flex; align-items: center; justify-content: center;
  }
  .brand-name {
    font-family: "Montserrat", sans-serif; font-weight: 600; color: var(--teal);
    display: flex; align-items: center; gap: 10px; letter-spacing: 0.5px;
  }
  .brand-name__dot { border-radius: 50%; border: 3px solid #9a9a9a; }
  .label__title {
    position: absolute; left: 0; width: 100%; background: var(--black);
    border-top: 2px solid var(--divider); border-bottom: 2px solid var(--divider);
    display: flex; align-items: center; justify-content: center;
    font-family: "Josefin Sans", sans-serif; font-weight: 300; letter-spacing: 1.5px;
  }

  .claims { position: absolute; left: 0; width: 100%; display: flex; align-items: center; justify-content: center; }
  .claims__word {
    font-family: "Montserrat", sans-serif; font-weight: 400; letter-spacing: 1.5px;
    border-top: 1px solid var(--white); border-bottom: 1px solid var(--white);
    padding: 3px 6px 2px;
  }
  .claims__emblem { display: flex; align-items: center; }

  .info-box { position: absolute; border: 1px solid var(--white); text-align: center; }
  .info-box__heading {
    font-family: "Josefin Sans", sans-serif; color: var(--ink); font-weight: 400;
    border-bottom: 1px solid var(--white);
  }
  .info-box__heading strong { font-weight: 600; }
  .features { list-style: none; font-weight: 300; }
  .features strong { font-weight: 600; }
  .info-box__footer { display: flex; align-items: center; gap: 6px; letter-spacing: 1px; }
  .info-box__footer::before, .info-box__footer::after { content: ""; flex: 1; height: 1px; background: var(--white); }

  .quality-badge {
    position: absolute; border: 1px solid var(--white); border-radius: 10px;
    text-align: center; font-weight: 300; line-height: 1.05;
  }

  /* Massage lotion */
  .label--massage { left: 133px; top: 62px; width: 420px; height: 414px; }
  .label--massage .label__top { height: 156px; }
  .label--massage .brand-name { font-size: 24px; }
  .label--massage .brand-name__dot { width: 22px; height: 22px; }
  .label--massage .label__title { top: 155px; height: 49px; font-size: 28px; padding-top: 4px; }
  .label--massage .claims { top: 226px; gap: 6px; }
  .label--massage .claims__word { font-size: 10px; width: 73px; text-align: center; }
  .label--massage .info-box { left: 103px; top: 274px; width: 214px; height: 112px; padding: 0 8px; }
  .label--massage .info-box__heading { font-size: 15px; padding: 6px 0 3px; }
  .label--massage .features { font-size: 9.5px; line-height: 17px; margin-top: 4px; }
  .label--massage .info-box__footer { font-size: 10px; margin-top: 5px; border-top: 1px solid var(--white); padding-top: 5px; }
  .label--massage .info-box__footer::before, .label--massage .info-box__footer::after { flex: 0 0 22px; }
  .label--massage .quality-badge { left: 333px; top: 338px; width: 47px; height: 47px; font-size: 12px; padding-top: 8px; }

  /* Topical pain lotion */
  .label--topical { left: 193px; top: 556px; width: 300px; height: 448px; }
  .label--topical .label__top { height: 175px; }
  .label--topical .brand-name { font-size: 20px; }
  .label--topical .brand-name__dot { width: 18px; height: 18px; }
  .label--topical .label__title { top: 174px; height: 48px; font-size: 18px; padding-top: 3px; }
  .label--topical .claims { top: 242px; gap: 4px; }
  .label--topical .claims__word { font-size: 9.5px; width: 62px; text-align: center; padding: 2px 2px 1px; }
  .label--topical .info-box { left: 62px; top: 293px; width: 177px; height: 30px; border-width: 1.5px; }
  .label--topical .info-box__heading { font-size: 17px; border: none; padding-top: 6px; }
  .label--topical .features { position: absolute; left: 0; top: 331px; width: 100%; text-align: center; font-size: 10.5px; line-height: 18.5px; }
  .label--topical .pain-note {
    position: absolute; left: 50%; top: 395px; transform: translateX(-50%);
    font-size: 10.5px; letter-spacing: 1px; padding: 4px 0 3px;
    border-top: 1px solid var(--white); border-bottom: 1px solid var(--white);
  }
</style>
</head>
<body>

  <p class="caption" style="top: 30px;">Massage lotion / Front side</p>

  <section class="label label--massage">
    <div class="label__top">
      <span class="brand-name"><span class="brand-name__dot"></span>QuillaBloom</span>
    </div>
    <h1 class="label__title">MASSAGE LOTION</h1>

    <div class="claims">
      <span class="claims__word">ORGANIC</span>
      <span class="claims__emblem">
        <svg width="56" height="32" viewBox="0 0 56 32" aria-hidden="true">
          <path d="M10 2 Q2 16 10 30" fill="none" stroke="#fff" stroke-width="1.6"/>
          <path d="M46 2 Q54 16 46 30" fill="none" stroke="#fff" stroke-width="1.6"/>
        </svg>
      </span>
      <span class="claims__word">NATURAL</span>
    </div>
    <div role="img" aria-label="Small white leaf emblem" style="position:absolute;left:199px;top:228px;width:22px;height:22px;border-radius:50%;background:var(--teal-light);"></div>

    <div class="info-box">
      <h2 class="info-box__heading"><strong>FACE &amp; BODY</strong> MASSAGE</h2>
      <ul class="features">
        <li>- <strong>Ultra</strong> Nourishing</li>
        <li>- For <strong>Body, Face</strong> and Massage</li>
        <li>- <strong>Rich in</strong> Antioxidats</li>
      </ul>
      <p class="info-box__footer">NANOTECHNOLOGICAL</p>
    </div>

    <div class="quality-badge">100%<br>quality</div>
  </section>

  <p class="caption" style="top: 524px;">Topical pain lotion / Front side</p>

  <section class="label label--topical">
    <div class="label__top">
      <span class="brand-name"><span class="brand-name__dot"></span>QuillaBloom</span>
    </div>
    <h1 class="label__title">TOPICAL PAIN LOTION</h1>

    <div class="claims">
      <span class="claims__word">ORGANIC</span>
      <span class="claims__emblem">
        <svg width="48" height="28" viewBox="0 0 48 28" aria-hidden="true">
          <path d="M8 2 Q1 14 8 26" fill="none" stroke="#fff" stroke-width="1.5"/>
          <path d="M40 2 Q47 14 40 26" fill="none" stroke="#fff" stroke-width="1.5"/>
        </svg>
      </span>
      <span class="claims__word">NATURAL</span>
    </div>
    <div role="img" aria-label="Small white leaf emblem" style="position:absolute;left:141px;top:246px;width:18px;height:18px;border-radius:50%;background:var(--teal-light);"></div>

    <div class="info-box">
      <h2 class="info-box__heading"><strong>MUSCLE</strong> CREAM</h2>
    </div>
    <ul class="features">
      <li>- <strong>Maximum</strong> Strength</li>
      <li>- Non-GMO &nbsp;| <strong>Gluten-Free</strong></li>
      <li>- <strong>Non-Greasy</strong></li>
    </ul>
    <p class="pain-note">PAIN-RELIEVING</p>
  </section>

</body>
</html>
```